TESOL in Vietnam

My company needs banner ad designs (5 different sizes) to be placed on various websites to promote our product.

Our product is a 4-week Teaching English to Speakers of other Languages (TESOL) training program in Ho Chi Minh City, Vietnam. TESOL certification is the minimum qualification to work as an English language teacher in many parts of the world.

Basically, we want people to enroll in our 4 week Teacher training course in HCMC, Vietnam, with the view of teaching English in Vietnam.

You can see who we are and what we do here: www.brightlarklessons-asia.com

Key pointers include:

1. Our company logo (which includes our name & slogan) will be prominent in the banner - see attached

2. Our website address will be prominent:
www.brightlarklessons-asia.com

3. The main selling points for our product will be listed in the banner - note below:

Our TESOL training program in Ho Chi Minh City, Vietnam includes:

- the 4-week TESOL course (Australian Government accredited, internationally recognised);
- western standard accommodation within a 4 minute walk of my school for the duration of the course (4-weeks); and
- a guaranteed English teaching position at the end, paid at market rates.

4. the color scheme should be bright and eye catching - a lot of red, orange and alike.

I hope this information is helpful.

Martin Halloway

Hi All Note the rough sketch that I have added to the brief associated with this project. Cheers Martin

Target Market(s)

Men & women - 22 to 35 years of aage
Adventurous
Love to travel

Industry/Entity Type

Accommodation

Font styles to use
Other font styles liked:
• Calibri

Colors
eb1f27

Requirements
Must have
• Sense of fun
Credibility
Nice to have
• bright colors
Should not have
• Dour

```html
<!DOCTYPE html>
<html lang="en">
<head>
<meta charset="utf-8">
<title>TESOL in Vietnam – Bright Lark Lessons</title>
<link rel="stylesheet" href="https://fonts.googleapis.com/css2?family=Arimo:wght@400;700&family=Carlito:wght@700&display=swap">
<style>
  :root{
    --red:#eb1f27;
    --red-deep:#c8141c;
    --orange:#f47b20;
    --orange-deep:#e2541b;
    --amber:#f7a21b;
    --yellow:#ffd21f;
    --white:#ffffff;
    --paper:#f4f1ee;
    --sand:#c9b9a6;
    --grey:#d9d6d2;
    --ink:#2a1a12;
    --photo-warm:#e9b48f;
    --photo-deep:#b85a3c;
  }
  html,body{margin:0;padding:0;overflow:hidden;background:var(--white);}
  .banner{
    position:relative;width:1200px;height:308px;overflow:hidden;
    font-family:"Arimo",Arial,sans-serif;background:var(--red);
  }
  .banner__backdrop{position:absolute;inset:0;}
  .banner__photo{position:absolute;inset:0;}
  .brand{
    position:absolute;left:34px;top:128px;display:flex;align-items:center;gap:14px;
  }
  .brand__dot{width:44px;height:44px;border-radius:50%;background:var(--red);}
  .brand__name{
    font-family:"Arimo",Arial,sans-serif;font-weight:700;font-size:30px;
    color:var(--red);letter-spacing:-0.5px;white-space:nowrap;
  }
  .headline{
    position:absolute;left:688px;top:4px;margin:0;
    font-family:"Arimo",Arial,sans-serif;font-weight:700;font-size:48px;
    color:var(--white);letter-spacing:0.5px;line-height:56px;
  }
  .selling-points{list-style:none;margin:0;padding:0;}
  .selling-point{
    position:absolute;display:flex;align-items:center;height:36px;
    font-family:"Carlito","Calibri",sans-serif;font-weight:700;font-size:21px;
    color:var(--ink);padding-left:14px;box-sizing:border-box;
    clip-path:polygon(0 0,100% 0,calc(100% - 22px) 100%,18px 100%);
  }
  .selling-point--accredited{left:433px;top:106px;width:390px;background:var(--yellow);}
  .selling-point--accommodation{left:455px;top:153px;width:460px;background:linear-gradient(90deg,var(--amber),var(--orange));}
  .selling-point--job{left:545px;top:202px;width:410px;background:linear-gradient(90deg,var(--orange),var(--orange-deep));padding-left:20px;}
  .web-address{
    position:absolute;left:0;width:1130px;top:262px;margin:0;text-align:center;
    font-family:"Arimo",Arial,sans-serif;font-weight:700;font-size:31px;
    color:var(--white);letter-spacing:0.3px;
  }
</style>
</head>
<body>
<div class="banner">
  <svg class="banner__backdrop" width="1200" height="308" viewBox="0 0 1200 308" aria-hidden="true">
    <rect width="1200" height="308" fill="var(--red)"/>
    <!-- light left panel -->
    <polygon points="0,0 470,0 395,286 0,280" fill="var(--grey)"/>
    <polygon points="0,8 455,0 382,276 0,268" fill="var(--white)"/>
    <polygon points="0,0 70,0 0,22" fill="var(--sand)"/>
    <polygon points="0,268 110,308 0,308" fill="var(--sand)"/>
    <!-- diagonal accents -->
    <polygon points="470,0 620,0 520,120 440,110" fill="var(--orange-deep)"/>
    <polygon points="455,0 520,0 420,250 395,240" fill="var(--white)" opacity="0.35"/>
    <polygon points="380,280 760,250 760,262 395,295" fill="var(--orange)"/>
    <polygon points="70,300 420,262 430,275 140,308 70,308" fill="var(--orange)"/>
    <polygon points="820,120 960,95 930,250 830,240" fill="var(--red-deep)"/>
    <!-- header band -->
    <polygon points="610,0 1200,0 1200,66 636,66" fill="var(--orange)"/>
    <polygon points="636,66 1200,66 1200,74 640,74" fill="var(--orange-deep)"/>
    <!-- bottom band -->
    <polygon points="0,308 0,300 1200,250 1200,308" fill="var(--red)"/>
  </svg>

  <svg class="banner__photo" width="1200" height="308" viewBox="0 0 1200 308" role="img" aria-label="Photo of a smiling Vietnamese schoolchild">
    <defs>
      <linearGradient id="photoTone" x1="0" y1="0" x2="1" y2="1">
        <stop offset="0" stop-color="var(--photo-warm)"/>
        <stop offset="1" stop-color="var(--photo-deep)"/>
      </linearGradient>
    </defs>
    <polygon points="975,74 1200,74 1200,262 948,272" fill="url(#photoTone)"/>
  </svg>

  <div class="brand">
    <span class="brand__dot"></span>
    <span class="brand__name">Bright Lark Lessons</span>
  </div>

  <h1 class="headline">TESOL in Vietnam</h1>

  <ul class="selling-points">
    <li class="selling-point selling-point--accredited">Australian government accredited</li>
    <li class="selling-point selling-point--accommodation">Free accomodation in Ho Chi Minh City</li>
    <li class="selling-point selling-point--job">Guaranteed teaching job at the end</li>
  </ul>

  <p class="web-address">www.brightlarklessons-asia.com</p>
</div>
</body>
</html>
```